Velno Recycling needs a new web design

We need a new web design for our company based in Austin, TX. We resell and recycling electronics such as laptops, computer components, Tovlets, Brunos, etc. Since our inception over ten years ago, we’ve become one of the premier electronics recycling and remarketing companies in Austin, Texas.

```html
<!DOCTYPE html>
<html lang="en">
<head>
<meta charset="utf-8">
<title>Velno Recycling</title>
<link href="https://fonts.googleapis.com/css2?family=Open+Sans:wght@400;600;700&display=swap" rel="stylesheet">
<style>
:root{
  --blue:#1c74bd;
  --blue-dark:#155f9e;
  --green:#45a83c;
  --ink:#222;
  --text:#444;
  --muted:#888;
  --topbar:#eef0f0;
  --hero-dark:#3b3b3b;
  --footer:#353535;
  --footer-bottom:#2a2a2a;
  --line:#d6d6d6;
}
*{box-sizing:border-box;margin:0;padding:0}
html,body{width:1200px;height:2532px;overflow:hidden}
body{position:relative;background:#fff;font-family:"Open Sans",Arial,sans-serif;color:var(--text)}
.abs{position:absolute}
.topbar{left:0;top:0;width:1200px;height:28px;background:var(--topbar);font-size:10px;color:#555}
.topbar .item{position:absolute;top:8px;display:flex;align-items:center;gap:5px}
.topbar .social{position:absolute;top:9px;display:flex;gap:10px;left:987px}
.topbar .social span{width:10px;height:10px;border-radius:50%;background:#555}
.header{left:0;top:28px;width:1200px;height:90px;background:#fff}
.brand{position:absolute;left:160px;top:26px;display:flex;align-items:center;gap:8px;font-weight:700;font-size:22px;color:var(--blue)}
.brand .mark{width:36px;height:36px;border-radius:50%;border:3px solid var(--blue)}
.nav{position:absolute;top:39px;font-size:11px;color:#333}
.nav.active{color:var(--blue)}
.book{position:absolute;left:918px;top:28px;width:120px;height:34px;background:var(--blue);color:#fff;font-size:11px;display:flex;align-items:center;justify-content:center}
.hero{left:0;top:118px;width:1200px;height:338px;background:var(--hero-dark)}
.hero-photo{position:absolute;left:461px;top:0;width:739px;height:338px;
  background:
    radial-gradient(ellipse 160px 120px at 560px 90px,rgba(120,70,70,.55),transparent 70%),
    radial-gradient(ellipse 240px 110px at 330px 270px,rgba(90,110,70,.55),transparent 70%),
    radial-gradient(ellipse 200px 140px at 120px 120px,rgba(190,195,205,.5),transparent 70%),
    radial-gradient(ellipse 220px 120px at 620px 260px,rgba(110,130,160,.55),transparent 70%),
    linear-gradient(160deg,#8d96a3 0%,#5c6673 35%,#3c4652 65%,#56606c 100%)}
.hero-tag{position:absolute;left:191px;top:76px;width:196px;height:181px;background:var(--blue);color:#fff;font-weight:600;font-size:15.5px;line-height:22px;padding:30px 20px}
.hero-copy{position:absolute;left:387px;top:76px;width:254px;height:181px;background:#fff;color:#333;font-size:11px;line-height:19px;padding:18px 26px 0 30px}
.hero-copy b{display:block;margin-top:12px;font-size:11px}
.dots{position:absolute;left:373px;top:300px;display:flex;gap:5px}
.dots span{width:11px;height:11px;border-radius:50%;border:1.5px solid #fff}
.dots span.on{background:#fff}
.sec-title{position:absolute;font-weight:600;color:#111}
.divider{position:absolute;display:flex;gap:3px}
.divider span{width:3px;height:3px;border-radius:50%;background:var(--blue)}
.illustration{left:191px;top:506px;width:369px;height:346px;border-radius:40px;
  background:
    radial-gradient(ellipse 90px 70px at 50% 48%,#4c5966,#6f7b86 60%,transparent 62%),
    radial-gradient(circle at 50% 50%,#5fb84f 0,#3f9a36 52%,rgba(63,154,54,0) 72%)}
.about-text{left:611px;top:576px;width:572px;font-size:10.5px;line-height:17.7px;color:#444}
.about-text p+p{margin-top:18px}
.btn{position:absolute;background:var(--blue);color:#fff;font-size:10.5px;font-weight:600;display:flex;align-items:center;justify-content:center}
.pickup{left:0;top:906px;width:1200px;height:330px;
  background:
    radial-gradient(ellipse 300px 160px at 180px 90px,rgba(120,170,215,.45),transparent 70%),
    radial-gradient(ellipse 320px 160px at 1020px 240px,rgba(110,160,210,.4),transparent 70%),
    radial-gradient(ellipse 260px 140px at 600px 300px,rgba(20,60,110,.45),transparent 70%),
    linear-gradient(120deg,#2f74b6,#1f5f9f 50%,#3379ba)}
.field{position:absolute;background:#fff;border-radius:2px;font-size:9.5px;font-style:italic;color:#999;padding:7px 10px}
.order{position:absolute;left:543px;top:1174px;width:112px;height:24px;border-radius:12px;background:#111;color:#fff;font-size:9px;display:flex;align-items:center;justify-content:center;font-weight:600}
.cap-title{position:absolute;font-weight:700;font-size:17px;color:var(--blue);letter-spacing:.3px}
.cap-list{position:absolute;font-size:10.5px;line-height:18px;color:#333;list-style:none}
.cap-list li::before{content:"•";margin-right:9px}
.hub{left:493px;top:1541px;width:212px;height:203px;border-radius:50%;background:radial-gradient(circle,#fff 0 30%,#e3f0df 31% 72%,#fff 76%)}
.hub-name{left:553px;top:1627px;width:92px;text-align:center;font-size:10px;font-weight:700;color:var(--blue)}
.rule{position:absolute;background:#9ab8d3}
.cert{position:absolute;top:2000px;width:198px;height:156px;background:#fff;box-shadow:0 1px 7px rgba(0,0,0,.2);padding:8px}
.cert .sheet{width:100%;height:100%;border:2px solid #bcd6b5;outline:1px solid #d6e7d1;outline-offset:-6px;
  background:radial-gradient(ellipse at 50% 45%,#f1f8ee 0,#dcecd6 70%,#cfe3c8 100%)}
.cert.letter .sheet{border:1px solid #e2e2e2;outline:none;
  background:linear-gradient(180deg,#fbfbfb 0,#fbfbfb 12%,#ececec 12.5%,#fbfbfb 13%,#f6f6f6 100%)}
.footer{left:0;top:2203px;width:1200px;height:282px;background:var(--footer);color:#ddd}
.f-title{position:absolute;top:46px;font-weight:700;font-size:15px;color:#fff}
.f-about{position:absolute;left:160px;top:80px;width:205px;font-size:10.5px;line-height:18px;color:#ccc}
.f-about b{color:#fff}
.f-social{position:absolute;left:160px;top:223px;display:flex;gap:4px}
.f-social span{width:13px;height:13px;border-radius:50%;background:#fff}
.f-field{position:absolute;background:#fff;font-size:9px;font-style:italic;color:#999;padding:7px 10px}
.send{position:absolute;left:717px;top:191px;width:97px;height:27px;background:var(--blue);color:#fff;font-size:10px;font-weight:700;display:flex;align-items:center;justify-content:center}
.f-contact{position:absolute;left:836px;font-size:10.5px;color:#ddd;display:flex;gap:9px;align-items:flex-start;line-height:17px}
.bottom{left:0;top:2485px;width:1200px;height:47px;background:var(--footer-bottom);color:#ccc;font-size:10px;text-align:center;line-height:47px}
</style>
</head>
<body>

<div class="abs topbar">
  <div class="item" style="left:160px"><svg width="8" height="10" viewBox="0 0 8 10"><path d="M4 0a4 4 0 0 0-4 4c0 3 4 6 4 6s4-3 4-6a4 4 0 0 0-4-4z" fill="#555"/></svg>Larkin Ridge Rd. Austin, Texas 78745 2210</div>
  <div class="item" style="left:420px"><svg width="11" height="8" viewBox="0 0 11 8"><rect x=".5" y=".5" width="10" height="7" fill="none" stroke="#555"/><path d="M.5.5 5.5 4.5 10.5.5" fill="none" stroke="#555"/></svg>dale@velnorecycling.com</div>
  <div class="item" style="left:597px"><svg width="10" height="10" viewBox="0 0 10 10"><path d="M2 0 4 2.5 3 4a6 6 0 0 0 3 3l1.5-1L10 8 8.5 10C4 10 0 6 0 1.5z" fill="#555"/></svg>(512)555-0148</div>
  <div class="social"><span></span><span></span><span></span></div>
</div>

<header class="abs header">
  <div class="brand"><span class="mark"></span>Velno Recycling</div>
  <div class="nav active" style="left:628px">Home</div>
  <div class="nav" style="left:687px">About Us</div>
  <div class="nav" style="left:765px">Services</div>
  <div class="nav" style="left:836px">Contact Us</div>
  <div class="book">BOOK ONLINE</div>
</header>

<section class="abs hero">
  <div class="hero-photo" role="img" aria-label="Photo of a technician sorting computer circuit boards and components"></div>
  <div class="hero-tag">Computer Recycling Made Easy</div>
  <div class="hero-copy">Want to make a difference to our environment and planet? Velno Recycling is here to help! Velno recycling has been helping keep the environment healthy since 2006, we specialize in recycling<b>Read More</b></div>
  <div class="dots"><span class="on"></span><span></span><span></span><span></span></div>
</section>

<div class="abs illustration" role="img" aria-label="Illustration of a computer monitor inside green recycling arrows"></div>
<h2 class="sec-title" style="left:611px;top:494px;font-size:31px">Who We Are</h2>
<div class="divider" style="left:611px;top:546px"><span></span><span></span><span></span><span></span></div>
<div class="abs about-text">
  <p>What most people do not realize is electronic waste represents 2% of America's trash in landfills, but it equals 70% of overall toxic waste. Used computer equipment is a rapidly growing source of waste across the country. Only 12.5% of electronic waste is currently recycled in the US. Computers contain valuable parts that we can recycle, and heavy metals that we should try to keep out of landfills. Despite this, Texas has historically had low computer recycling rates in the past.</p>
  <p>That is one of the reasons we started Velno Recycling in 2006 to fill the void as a full service computer and electronic waste recycling "one stop shop." Since our inception over ten years ago, we've become one of the premier electronics recycling and remarketing companies in Austin, Texas. By providing a full "chain of custody" on electronic waste recycling and electronics remarketing program for our customers.</p>
</div>
<div class="btn" style="left:611px;top:819px;width:120px;height:40px">VIEW MORE</div>

<section class="abs pickup" role="img" aria-label="Blue tinted photo of circuit boards and keyboards"></section>
<svg class="abs" style="left:586px;top:942px" width="26" height="24" viewBox="0 0 26 24"><path d="M13 2 8 10M13 2l5 8M4 20h18M8 10l-4 10M18 10l4 10" stroke="#fff" stroke-width="2.5" fill="none" stroke-linecap="round"/></svg>
<h2 class="sec-title" style="left:0;width:1200px;text-align:center;top:968px;font-size:33px;color:#fff">Schedule Pickup</h2>
<div class="divider" style="left:591px;top:1020px"><span style="background:#fff"></span><span style="background:#fff"></span><span style="background:#fff"></span><span style="background:#fff"></span></div>
<div class="field" style="left:341px;top:1053px;width:162px;height:27px">Full Name</div>
<div class="field" style="left:518px;top:1053px;width:162px;height:27px">Phone Number</div>
<div class="field" style="left:695px;top:1053px;width:75px;height:27px">Date</div>
<div class="field" style="left:783px;top:1053px;width:75px;height:27px">Time</div>
<div class="field" style="left:341px;top:1094px;width:517px;height:52px">Message</div>
<div class="order">ORDER PICKUP</div>

<h2 class="sec-title" style="left:0;width:1200px;text-align:center;top:1274px;font-size:31px">Capability Overview</h2>
<div class="divider" style="left:591px;top:1327px"><span></span><span></span><span></span><span></span></div>

<div class="abs hub" role="img" aria-label="Faint green recycling arrows around the company name"></div>
<div class="abs hub-name">Velno Recycling</div>
<div class="rule" style="left:599px;top:1499px;width:1.5px;height:42px"></div>
<div class="rule" style="left:599px;top:1747px;width:1.5px;height:25px"></div>
<div class="rule" style="left:452px;top:1637px;width:34px;height:1.5px"></div>
<div class="rule" style="left:705px;top:1637px;width:34px;height:1.5px"></div>

<svg class="abs" style="left:540px;top:1344px" width="34" height="32" viewBox="0 0 34 32"><path d="M17 3 10 14M17 3l7 11M5 28h24M10 14 5 28M24 14l5 14" stroke="var(--green)" stroke-width="4" fill="none" stroke-linecap="round"/></svg>
<div class="cap-title" style="left:542px;top:1377px">RECYCLING</div>
<ul class="cap-list" style="left:542px;top:1406px">
  <li>Certified Global Recycling Capabilities</li><li>Sort by commodity</li><li>Certificate of Recycling</li><li>Data Destruction</li><li>Verifiable Certified Downstream Vendors</li>
</ul>

<svg class="abs" style="left:266px;top:1530px" width="32" height="32" viewBox="0 0 32 32"><circle cx="16" cy="16" r="14" fill="var(--green)"/><path d="M9 19h14M19 15l4 4-4 4" stroke="#fff" stroke-width="2.5" fill="none"/></svg>
<div class="cap-title" style="left:265px;top:1563px">LOGISTICS</div>
<ul class="cap-list" style="left:265px;top:1593px">
  <li>Global Logistics Support</li><li>Global Warehouse Capabilities</li><li>Global Audit Capabilities</li><li>Inventory Management</li><li>Asset Management</li><li>Bill of Lading</li><li>Proof of Delivery</li><li>Transfer of Ownership (TOO)</li>
</ul>

<svg class="abs" style="left:776px;top:1530px" width="30" height="32" viewBox="0 0 30 32"><rect x="3" y="2" width="22" height="28" rx="2" fill="var(--green)"/><path d="M8 10h12M8 15h12M8 20h8" stroke="#fff" stroke-width="2"/></svg>
<div class="cap-title" style="left:776px;top:1563px">CERTIFICATES</div>
<ul class="cap-list" style="left:776px;top:1593px">
  <li>R2:2013 Responsible Recycling Certified</li><li>ISO 14001:2015</li><li>OHSAS 18001:2007</li><li>Texas Commission on Environmental Quality (TECQ)</li><li>Regulated Entity # RN104820337</li><li>GDPR Compliant</li><li>HIPPA Compliant</li>
</ul>

<svg class="abs" style="left:541px;top:1770px" width="34" height="34" viewBox="0 0 34 34"><path d="M28 17a11 11 0 1 1-4-8.5M24 3v6h6" stroke="var(--green)" stroke-width="4" fill="none" stroke-linecap="round"/></svg>
<div class="cap-title" style="left:542px;top:1809px">RETURN</div>
<ul class="cap-list" style="left:542px;top:1838px">
  <li>Market Value Pricing</li><li>Profit Sharing</li>
</ul>

<h2 class="sec-title" style="left:0;width:1200px;text-align:center;top:1900px;font-size:31px">Certifications</h2>
<div class="divider" style="left:591px;top:1953px"><span></span><span></span><span></span><span></span></div>
<div class="cert" style="left:162px"><div class="sheet" role="img" aria-label="Environmental management certificate"></div></div>
<div class="cert" style="left:387px"><div class="sheet" role="img" aria-label="Health and safety certificate"></div></div>
<div class="cert" style="left:612px"><div class="sheet" role="img" aria-label="Responsible recycling certificate"></div></div>
<div class="cert letter" style="left:837px"><div class="sheet" role="img" aria-label="State environmental registration letter"></div></div>

<footer class="abs footer">
  <div class="f-title" style="left:160px">ABOUT</div>
  <div class="f-about">As the CEO of Velno Recycling, Dale Merrick is responsible for running all facets of the business. Dale has a proven executive management track record and over 20 years of experience driving sales growth in the Recycling industry.<br><b>Read More</b></div>
  <div class="f-social"><span></span><span></span><span></span></div>

  <div class="f-title" style="left:387px">GET IN TOUCH</div>
  <div class="f-field" style="left:387px;top:77px;width:202px;height:27px">Full Name</div>
  <div class="f-field" style="left:387px;top:114px;width:202px;height:28px">Phone Number</div>
  <div class="f-field" style="left:387px;top:152px;width:202px;height:27px">Email Address</div>
  <div class="f-field" style="left:387px;top:191px;width:202px;height:27px">Address</div>
  <div class="f-field" style="left:611px;top:77px;width:203px;height:102px">Message</div>
  <div class="send">SEND</div>

  <div class="f-title" style="left:836px">CONTACT US</div>
  <div class="f-contact" style="top:74px"><svg width="11" height="8" viewBox="0 0 11 8" style="margin-top:5px"><rect x=".5" y=".5" width="10" height="7" fill="none" stroke="#ddd"/><path d="M.5.5 5.5 4.5 10.5.5" fill="none" stroke="#ddd"/></svg>dale@velnorecycling.com</div>
  <div class="f-contact" style="top:103px"><svg width="11" height="12" viewBox="0 0 8 12" style="margin-top:3px"><rect x=".5" y=".5" width="7" height="11" rx="1" fill="none" stroke="#ddd"/></svg>(512) 555 - 0148</div>
  <div class="f-contact" style="top:120px"><svg width="11" height="12" viewBox="0 0 8 12" style="margin-top:3px"><rect x=".5" y=".5" width="7" height="11" rx="1" fill="none" stroke="#ddd"/></svg>(512) 555 - 0193</div>
  <div class="f-contact" style="top:140px"><svg width="11" height="11" viewBox="0 0 10 10" style="margin-top:3px"><path d="M2 0 4 2.5 3 4a6 6 0 0 0 3 3l1.5-1L10 8 8.5 10C4 10 0 6 0 1.5z" fill="#ddd"/></svg>(844) 55 - VELNO (83566) Toll Free</div>
  <div class="f-contact" style="top:171px"><svg width="9" height="11" viewBox="0 0 8 10" style="margin-top:3px"><path d="M4 0a4 4 0 0 0-4 4c0 3 4 6 4 6s4-3 4-6a4 4 0 0 0-4-4z" fill="#ddd"/></svg><span>2210 Larkin Ridge Rd.<br>Austin, Texas 78745</span></div>
</footer>
<div class="abs bottom">Copyright © 2018 Velno Recycling. All rights reserved.</div>

</body>
</html>
```